Wine label refresh

We are wanting to modify our Corran Hollow label to include a picture on it.
I have attached the pictures below which we would like on the label. They are of the Corran Hollow vineyard. I have also attached an example of another label with a picture on it that we like the style of.
Updates
Industry/Entity Type
Vineyard
Requirements
Must have
- The Corran Hollow text must stay the same but can be moved down. It still needs to be the same size though.
Marlborough Sauvignon Blanc should remain in the same font and roughly the same size.
Wine of New Zealand also must stay but could potentially be moved.
Nice to have
- It would be nice if we could keep the PM logo on the front label but feel free to experiment with where this goes.

```html
<!DOCTYPE html>
<html lang="en">
<head>
<meta charset="utf-8">
<title>Corran Hollow – Marlborough Sauvignon Blanc Label</title>
<link rel="stylesheet" href="https://fonts.googleapis.com/css2?family=Cormorant+Garamond:wght@500&family=Pinyon+Script&family=Lato:wght@400&display=swap">
<style>
  :root {
    --page: #f4f3ef;
    --label-white: #fbfbf9;
    --panel-cream: #f3f0ec;
    --ink: #2a2624;
    --wine-red: #8e1d1b;
    --script-cream: #f6e9dc;
    --muted: #aaa49e;
    --gold-light: #f7ead9;
    --gold-mid: #d9b89c;
    --gold-dark: #b98f72;
    --sky: #dfe2df;
    --hills: #a8b3a2;
    --vines: #5e8a45;
    --vines-deep: #3f6a2e;
  }
  * { margin: 0; padding: 0; box-sizing: border-box; }
  html, body {
    width: 1200px; height: 2420px; overflow: hidden;
    background: var(--page);
  }
  .label {
    position: absolute; left: 80px; top: 695px;
    width: 1040px; height: 1030px;
    background: var(--label-white);
    box-shadow: 0 2px 10px rgba(0,0,0,0.08);
  }
  .foil-band {
    position: absolute; left: 0; width: 100%; height: 40px;
    background: linear-gradient(90deg, var(--gold-dark), var(--gold-light) 18%, var(--gold-mid) 40%, var(--gold-light) 62%, var(--gold-dark) 82%, var(--gold-light));
  }
  .foil-band--top { top: 50px; }
  .foil-band--bottom { top: 945px; }
  .panel {
    position: absolute; left: 18px; right: 18px; top: 90px; height: 855px;
    background: var(--panel-cream);
    border-left: 16px solid var(--gold-mid);
    border-right: 16px solid var(--gold-mid);
  }
  .monogram {
    position: absolute; top: 60px; width: 100%; text-align: center;
    font-family: "Cormorant Garamond", serif; font-weight: 500;
    font-size: 120px; line-height: 1; color: var(--ink); letter-spacing: -4px;
  }
  .estate-name {
    position: absolute; top: 270px; width: 100%; text-align: center;
    font-family: "Cormorant Garamond", serif; font-weight: 500;
    font-size: 82px; line-height: 1; color: var(--ink);
    font-variant: small-caps; letter-spacing: 3px;
  }
  .vineyard-view {
    position: absolute; top: 370px; left: 0; right: 0; height: 220px;
    background: linear-gradient(180deg, var(--sky) 0%, var(--sky) 28%, var(--hills) 42%, var(--vines) 58%, var(--vines-deep) 78%, var(--vines) 100%);
  }
  .variety-band {
    position: absolute; top: 590px; left: 0; right: 0; height: 172px;
    background: var(--wine-red);
    text-align: center; color: var(--script-cream);
    font-family: "Pinyon Script", cursive; font-size: 62px; line-height: 76px;
    padding-top: 12px;
  }
  .label-details {
    position: absolute; top: 790px; left: 20px; right: 20px;
    display: flex; justify-content: space-between;
    font-family: "Lato", sans-serif; font-size: 26px; color: var(--muted);
    letter-spacing: 1px;
  }
</style>
</head>
<body>
  <main class="label">
    <div class="foil-band foil-band--top"></div>
    <section class="panel">
      <div class="monogram">PM</div>
      <h1 class="estate-name">Corran Hollow</h1>
      <div class="vineyard-view" role="img" aria-label="Photograph of the Corran Hollow vineyard: rows of green vines leading to a homestead under a misty sky"></div>
      <div class="variety-band">
        <p>Marlborough Sauvignon Blanc</p>
        <p>2012</p>
      </div>
      <div class="label-details">
        <span>750ml</span>
        <span>NEW ZEALAND WINE</span>
        <span>13% alc/vol</span>
      </div>
    </section>
    <div class="foil-band foil-band--bottom"></div>
  </main>
</body>
</html>
```